Business card for Northway's Blue Wagon.

Good day i am looking for a business card design for my business.
The name of the business is Northway's Blue Wagon. It is a van rental business that provides a driver and helper to the customer. Customer have use to van for small moves, studio or 1 bedroom, Moving furniture like couch or kitchen cabinets.
We are available evenings, weekends and holidays.
the means to contact us is by phone at 614-927-3048; By emails at Kestrel@northwaysbluewagon-example.com; or by social media, Facebook and Instagram.
You can see attached pictures of the van and or logo.

```html
<!DOCTYPE html>
<html lang="en">
<head>
<meta charset="UTF-8">
<title>Northway's Blue Wagon – Business Card</title>
<link rel="stylesheet" href="https://fonts.googleapis.com/css2?family=Montserrat:wght@500;600;700&display=swap">
<style>
  :root {
    --stage: #353535;
    --card-white: #ffffff;
    --brand-red: #d42027;
    --ink: #111111;
    --faint: #ececee;
  }
  * { margin: 0; padding: 0; box-sizing: border-box; }
  html, body {
    width: 1200px; height: 1200px; overflow: hidden;
    background: var(--stage);
    font-family: "Montserrat", Arial, sans-serif;
  }
  .canvas { position: relative; width: 1200px; height: 1200px; }

  .card {
    position: absolute; left: 217px; width: 772px; height: 462px;
    overflow: hidden;
    box-shadow: 0 6px 18px rgba(0,0,0,0.45);
  }
  .card--front { top: 107px; background: var(--card-white); }
  .card--back { top: 635px; background: var(--brand-red); }

  .front__mark {
    position: absolute; left: 330px; top: 120px; width: 420px;
    text-align: center;
    font-weight: 700; font-size: 46px; line-height: 1.15;
    color: var(--faint);
  }

  .front__wave { position: absolute; inset: 0; width: 772px; height: 462px; }

  .identity { position: absolute; left: 54px; top: 52px; }
  .identity__name { font-weight: 700; font-size: 34px; color: var(--ink); line-height: 1.1; }
  .identity__title { font-weight: 600; font-size: 22px; color: var(--ink); margin-top: 14px; }

  .contacts { position: absolute; left: 54px; top: 221px; list-style: none; }
  .contacts__item {
    display: flex; align-items: center; height: 24px;
    font-weight: 500; font-size: 20px; color: var(--ink);
    margin-bottom: 14px;
  }
  .contacts__item:nth-child(2) { margin-bottom: 16px; }
  .contacts__icon { width: 24px; height: 24px; margin-right: 9px; flex: none; }
  .contacts__dot {
    width: 24px; height: 24px; border-radius: 50%;
    background: var(--ink); margin-right: 9px; flex: none;
  }

  .tagline {
    position: absolute; left: 0; right: 0; top: 385px;
    text-align: center;
    font-weight: 500; font-size: 19px; letter-spacing: 0.2em;
    color: var(--card-white);
  }

  .back__name {
    position: absolute; left: 0; right: 0; top: 205px;
    text-align: center;
    font-weight: 700; font-size: 40px;
    color: var(--card-white);
  }
</style>
</head>
<body>
<main class="canvas">

  <section class="card card--front">
    <div class="front__mark" aria-hidden="true">Northway's Blue Wagon</div>

    <svg class="front__wave" viewBox="0 0 772 462" aria-hidden="true">
      <path fill="#d42027" d="M0 331 C60 360 120 372 170 371 C330 368 430 310 576 307 C660 305 720 325 772 349 L772 462 L0 462 Z"/>
    </svg>

    <div class="identity">
      <h1 class="identity__name">Your Name</h1>
      <p class="identity__title">Your Title</p>
    </div>

    <ul class="contacts">
      <li class="contacts__item">
        <svg class="contacts__icon" viewBox="0 0 24 24" aria-label="Phone">
          <circle cx="12" cy="12" r="12" fill="#111"/>
          <path fill="#fff" d="M8.2 6.2c.4-.3.9-.2 1.2.2l1.2 1.8c.3.4.2.9-.1 1.2l-.8.7c.6 1.4 1.7 2.6 3.1 3.3l.7-.8c.3-.4.8-.4 1.2-.2l1.8 1.2c.4.3.5.8.2 1.2l-.9 1.2c-.4.5-1.1.7-1.7.5-3.3-1.1-5.8-3.6-6.8-6.9-.2-.6 0-1.3.5-1.7z"/>
        </svg>
        614-927-3048
      </li>
      <li class="contacts__item">
        <svg class="contacts__icon" viewBox="0 0 24 24" aria-label="Email">
          <circle cx="12" cy="12" r="12" fill="#111"/>
          <rect x="6" y="8" width="12" height="8.5" rx="1" fill="#fff"/>
          <path d="M6.5 8.6 12 12.8 17.5 8.6" fill="none" stroke="#111" stroke-width="1.2"/>
        </svg>
        Kestrel@northwaysbluewagon-example.com
      </li>
      <li class="contacts__item">
        <span class="contacts__dot" aria-hidden="true"></span>
        @northwaysbluewagon-example.com
      </li>
    </ul>

    <p class="tagline">We are available in evenings, weekends and holidays</p>
  </section>

  <section class="card card--back">
    <p class="back__name">Northway's Blue Wagon</p>
  </section>

</main>
</body>
</html>
```